Postcard design to acquire new clients for my Property Management Company

I'm looking for a postcard design that I can send to prospective clients detailing information about my company and services.
Postcard should be eye catching and contain information from www.brightkeyrentals-example.com. I've provided a few screen shots for the most important information and my logo.
Target Market(s)
Real Estate
Industry/Entity Type
Real Estate
Font styles to use
Sans Serif
Requirements
Must have
- Must be eye catching!! this will be a direct mail piece - I'd like for the card to be read and not tossed in the trash immediately.
Design que from the logo.
A place to write / print the receipts name and address.
our physical address - 2287 Marble Lane, Lubbock, TX 79555.
Should not have
- the contact information on the business card is not accurate - please use info from website.

```html
<!DOCTYPE html>
<html lang="en">
<head>
<meta charset="utf-8">
<title>BrightKey Rentals – Direct Mail Postcard</title>
<link rel="stylesheet" href="https://fonts.googleapis.com/css2?family=Montserrat:wght@400;500;600;700&display=swap">
<style>
  :root{
    --navy:#064a79;
    --navy-text:#0a4b7d;
    --band-grey:#a3a4a6;
    --panel-grey:#e2e3e5;
    --mail-grey:#c4c4c4;
    --paper:#f4f4f4;
    --ink:#222;
    --muted:#8a8c90;
    --backdrop:#e6e6e6;
    --photo-sky:#3f6fa6;
    --photo-mid:#6a5f7c;
    --photo-warm:#d9604d;
  }
  *{box-sizing:border-box;margin:0;padding:0}
  html,body{width:1200px;height:1200px;overflow:hidden}
  body{background:var(--backdrop);font-family:"Montserrat",Arial,sans-serif;color:var(--ink);position:relative}

  .postcard{position:absolute;left:267px;width:666px;height:444px;background:var(--paper);overflow:hidden}
  .postcard--front{top:118px}
  .postcard--back{top:638px}
  .postcard svg.shapes{position:absolute;inset:0;width:100%;height:100%}
  .abs{position:absolute;white-space:nowrap}

  /* front */
  .brand-name{left:43px;top:28px;font-size:30px;font-weight:600;letter-spacing:5px;line-height:36px;color:var(--navy-text)}
  .services-heading{left:43px;top:118px;color:#fff;font-size:15.5px;font-weight:700;letter-spacing:.2px}
  .services-sub{left:43px;top:137px;color:#fff;font-size:11.5px;font-weight:500}
  .service-list{left:42px;top:176px;list-style:none}
  .service-list li{display:flex;align-items:center;height:25.1px;color:#fff;font-size:12.2px;font-weight:500;letter-spacing:.6px}
  .service-list svg{width:16px;height:14px;margin-right:13px;fill:#b9c8d6}
  .web-front{left:43px;top:402px;font-size:11px;font-weight:500;color:var(--ink)}
  .web-front b,.web-back b{font-weight:700}
  .web-front b{color:var(--navy-text)}
  .hero-title{right:27px;top:268px;text-align:right;color:#fff;font-size:23.5px;font-weight:700;line-height:32.5px}
  .hero-sub{right:27px;top:380px;text-align:right;color:#fff;font-size:15px;font-weight:400;line-height:19.5px}

  /* back */
  .back-heading{left:0;right:0;top:23px;text-align:center;color:var(--navy-text);font-size:15px;font-weight:700}
  .back-sub{left:0;right:0;top:43px;text-align:center;font-size:11.5px;font-weight:500}
  .plan{position:absolute;width:201px;background:var(--panel-grey);text-align:center;padding-top:10px}
  .plan--lease{left:19px;top:84px;height:226px}
  .plan--full{left:232px;top:69px;height:241px}
  .plan--premium{left:446px;top:84px;height:226px}
  .plan h2{font-size:15.5px;font-weight:700;color:var(--navy-text);line-height:20px}
  .plan .tag{font-size:10px;color:var(--muted);margin-top:2px}
  .plan .rate{font-size:24px;font-weight:700;color:var(--navy-text);line-height:24px;margin-top:2px}
  .plan .basis{font-size:10px;color:var(--muted);line-height:12px}
  .plan ul{list-style:none;margin-top:10px;font-size:10.3px;font-weight:500;line-height:17px;color:var(--ink)}
  .brand-back{left:36px;top:318px;font-size:18px;font-weight:600;letter-spacing:2.5px;color:#fff}
  .phone{left:36px;top:343px;font-size:21px;font-weight:700;letter-spacing:1.5px;color:#fff}
  .email{left:36px;top:373px;font-size:11px;color:#fff}
  .web-back{left:36px;top:390px;font-size:11px;color:#fff}
  .address{left:36px;top:408px;font-size:10.5px;color:#fff}
</style>
</head>
<body>

<section class="postcard postcard--front" aria-label="Postcard front">
  <svg class="shapes" viewBox="0 0 666 444">
    <defs>
      <linearGradient id="photoTone" x1="0" y1="0" x2="0" y2="1">
        <stop offset="0" stop-color="var(--photo-sky)"/>
        <stop offset=".55" stop-color="var(--photo-mid)"/>
        <stop offset="1" stop-color="var(--photo-warm)"/>
      </linearGradient>
    </defs>
    <polygon points="0,109 402,109 378,162 0,162" fill="var(--band-grey)"/>
    <polygon points="0,162 372,162 275,386 0,386" fill="var(--navy)"/>
    <polygon role="img" aria-label="Photo of a Lubbock office building at dusk under a blue sky" points="451,0 666,0 666,444 258,444" fill="url(#photoTone)"/>
  </svg>

  <div class="abs brand-name">BRIGHTKEY<br>RENTALS</div>
  <div class="abs services-heading">DISCOVER OUR SERVICES</div>
  <div class="abs services-sub">We offer full-service property management solutions</div>

  <ul class="abs service-list">
    <li><svg viewBox="0 0 16 14"><path d="M8 1 1 7h2v6h4V9h2v4h4V7h2z"/></svg>PROPERTY MARKETING</li>
    <li><svg viewBox="0 0 16 14"><circle cx="5" cy="4" r="2.6"/><circle cx="11.5" cy="4" r="2.3"/><path d="M0 13c0-3.5 2-5 5-5s5 1.5 5 5zM10.5 8c3 0 5.5 1.2 5.5 5h-4.5c0-2-.4-3.6-1-5z"/></svg>TENANT SCREENING</li>
    <li><svg viewBox="0 0 16 14"><path d="M8.8 0v1.6c1.5.2 2.6.9 3 2.3l-1.7.6c-.3-.8-1-1.2-2-1.2-1.1 0-1.7.5-1.7 1.1 0 .8.8 1 2.2 1.4 1.8.5 3.2 1.1 3.2 2.9 0 1.4-1 2.4-3 2.7V14H7.3v-1.6c-1.7-.2-2.9-1.1-3.2-2.6l1.8-.5c.3 1 1.1 1.5 2.3 1.5 1.2 0 1.8-.5 1.8-1.2 0-.8-.8-1.1-2.3-1.5-1.6-.4-3-1-3-2.8 0-1.300 1-2.3 2.6-2.6V0z"/></svg>RENT COLLECTION</li>
    <li><svg viewBox="0 0 16 14"><path d="M9 1l3-1 4 4-2 2-2-1-8 9-3-1 9-8z"/></svg>MAINTENANCE</li>
    <li><svg viewBox="0 0 16 14"><path d="M6 0a5.5 5.5 0 0 1 4.6 8.5l4 4-1.5 1.5-4-4A5.5 5.5 0 1 1 6 0zm0 2a3.5 3.5 0 1 0 0 7 3.5 3.5 0 0 0 0-7z"/></svg>PROPERTY INSPECTIONS</li>
    <li><svg viewBox="0 0 16 14"><path d="M1 0h1v12h14v1H1zM4 7h1.5v4H4zM7 4h1.5v7H7zM10 6h1.5v5H10zM13 3h1.5v8H13z"/></svg>FINANCIAL REPORTING</li>
    <li><svg viewBox="0 0 16 14"><path d="M8 0l6 2v4c0 4-3 7-6 8-3-1-6-4-6-8V2z"/></svg>EVICTIONS</li>
    <li><svg viewBox="0 0 16 14"><path d="M7.3 0h1.4v2h5v1.2l2.3 5.3c0 1.4-1.3 2.3-2.7 2.3s-2.7-.9-2.7-2.3L12.8 3.2H8.7V12h3v2H4.3v-2h3V3.2H3.2l2.2 5.3c0 1.4-1.3 2.3-2.7 2.3S0 9.9 0 8.5l2.3-5.3V2h5zM2.7 4.6 1.3 8h2.8zm10.6 0L11.9 8h2.8z"/></svg>LEGAL GUIDANCE</li>
  </ul>

  <div class="abs web-front">www.<b>brightkeyrentals-example</b>.com</div>

  <h1 class="abs hero-title">PROPERTY<br>MANAGEMENT ACROSS<br>LUBBOCK, TX</h1>
  <p class="abs hero-sub">Maximize your financial returns with<br>support from our rental specialists</p>
</section>

<section class="postcard postcard--back" aria-label="Postcard back">
  <svg class="shapes" viewBox="0 0 666 444">
    <polygon points="0,310 360,310 300,444 0,444" fill="var(--navy)"/>
    <polygon points="385,310 666,310 666,444 325,444" fill="var(--mail-grey)"/>
    <g stroke="#fff" stroke-width="1">
      <line x1="430" y1="359" x2="636" y2="359"/>
      <line x1="430" y1="388" x2="636" y2="388"/>
      <line x1="430" y1="416" x2="636" y2="416"/>
    </g>
  </svg>

  <h2 class="abs back-heading">CHOOSE THE RIGHT PROPERTY MANAGEMENT SYSTEM</h2>
  <p class="abs back-sub">Selecting the wrong manager could be your costliest mistake ever.</p>

  <article class="plan plan--lease">
    <h2>Lease Only</h2>
    <p class="tag">- You Just Need Tenants -</p>
    <p class="rate">9%</p>
    <p class="basis">of annual lease</p>
    <ul>
      <li>Professional Photography</li>
      <li>Marketing &amp; Advertising</li>
      <li>Property Showings</li>
      <li>Tenant Screening &amp; Qualifications</li>
      <li>Lease Execution</li>
      <li>Move In Coordination</li>
    </ul>
  </article>

  <article class="plan plan--full">
    <h2>Full Service</h2>
    <p class="tag">- Our Most Popular -</p>
    <p class="rate">10%</p>
    <p class="basis">of monthly rent</p>
    <ul>
      <li>Includes Leasing Service</li>
      <li>24/7 Emergency Response</li>
      <li>Move In &amp; Out Inspections</li>
      <li>Professional Lease Enforcement</li>
      <li>Schedule &amp; Oversee all Repairs</li>
      <li>Pay all Invoices</li>
      <li>Monthly &amp; Year End Statements</li>
      <li>Annual Market Rent Analysis</li>
    </ul>
  </article>

  <article class="plan plan--premium">
    <h2>Premium Service</h2>
    <p class="tag">- Our Premier Service -</p>
    <p class="rate">12%</p>
    <p class="basis">of monthly rent</p>
    <ul>
      <li>Includes Full Service Features</li>
      <li>Professional Video Marketing</li>
      <li>Home Warranty Coordination</li>
      <li>Tenant Retention Program</li>
    </ul>
  </article>

  <div class="abs brand-back">BRIGHTKEY RENTALS</div>
  <div class="abs phone">(806) 555-0147</div>
  <div class="abs email">info@brightkeyrentals-example.com</div>
  <div class="abs web-back">www.<b>brightkeyrentals-example</b>.com</div>
  <div class="abs address">2287 Marble Lane, Lubbock, TX 79555</div>
</section>

</body>
</html>
```